Satin Decor Paint Label

We will have three different sizes for this label but the dimensions for the medium size are 2" tall by 11.75'' wide. Please work off that.

Our colors are typically black and white but feel free to incorporate silver, gold, bronze or any combination. We would like to see multiple color variations of your designs.

General Info needed on label:
2736
Coatings
Interior Decor Paint
Furniture, Trim, Cabinets
Acrylic Waterborne Urethane
Satin Finish
16 FL. OZ. - 473 mL
````````````````````````````````````````````````````````````````````````````````````````````
Your design does not have to be the same as the one in the attached image.

You can put Satin Finish or Interior Decor Paint or something else going vertically up the side.

The label will be on a container like the the one in the attached image. Please have your design work on the same container.

```html
<!DOCTYPE html>
<html lang="en">
<head>
<meta charset="utf-8">
<title>2736 Coatings – Interior Decor Paint Label</title>
<link href="https://fonts.googleapis.com/css2?family=Montserrat:wght@400;600;700&display=swap" rel="stylesheet">
<style>
  :root {
    --label-black: #000000;
    --ink-white: #ffffff;
    --page-white: #ffffff;
    --wall-grey: #8d8d92;
    --linen-grey: #9c9ca1;
    --throw-rose: #8a6c6c;
  }
  html, body {
    margin: 0;
    padding: 0;
    width: 839px;
    height: 1200px;
    overflow: hidden;
    background: var(--page-white);
  }
  .canvas {
    position: relative;
    width: 839px;
    height: 1200px;
  }
  .label {
    position: absolute;
    left: 113px;
    top: 440px;
    width: 627px;
    height: 321px;
    background: var(--label-black);
    overflow: hidden;
    font-family: "Montserrat", sans-serif;
    color: var(--ink-white);
  }
  .brand {
    position: absolute;
    left: 20px;
    top: 36px;
    width: 304px;
    text-align: center;
    font-weight: 600;
    color: var(--ink-white);
    line-height: 1;
  }
  .brand-number {
    display: block;
    font-size: 104px;
    letter-spacing: 2px;
  }
  .brand-word {
    display: block;
    margin-top: 8px;
    font-size: 30px;
    letter-spacing: 12px;
    padding-left: 12px;
  }
  .product-name {
    position: absolute;
    left: 10px;
    top: 208px;
    width: 324px;
    text-align: center;
    font-weight: 700;
    font-size: 20px;
    letter-spacing: 0.5px;
  }
  .uses {
    position: absolute;
    left: 10px;
    top: 250px;
    width: 324px;
    text-align: center;
    font-weight: 400;
    font-size: 13px;
    letter-spacing: 0.6px;
  }
  .volume {
    position: absolute;
    left: 10px;
    top: 281px;
    width: 324px;
    text-align: center;
    font-weight: 700;
    font-size: 12px;
  }
  .photo-tiles {
    position: absolute;
    left: 0;
    top: 0;
  }
  .specs {
    position: absolute;
    right: 14px;
    top: 130px;
    text-align: right;
    font-weight: 700;
    font-size: 10px;
    line-height: 12.5px;
    letter-spacing: 0.3px;
  }
</style>
</head>
<body>
<div class="canvas">
  <div class="label">
    <svg class="photo-tiles" width="627" height="321" viewBox="0 0 627 321" role="img" aria-label="Bedroom interior photograph shown in diamond tiles: grey wall, grey pillows, rust cushion and rose bedspread">
      <polygon points="314,182 419,77 524,182 419,287" fill="var(--wall-grey)"/>
      <polygon points="418,60 510,-32 612,60 510,162" fill="var(--linen-grey)"/>
      <polygon points="418,260 510,168 612,260 510,362" fill="var(--throw-rose)"/>
    </svg>
    <div class="brand">
      <span class="brand-number">2736</span>
      <span class="brand-word">COATINGS</span>
    </div>
    <div class="product-name">INTERIOR DECOR PAINT</div>
    <div class="uses">FURNITURE&nbsp; | &nbsp;TRIM&nbsp; | &nbsp;CABINETS</div>
    <div class="volume">16 FL. OZ. - 473 mL</div>
    <div class="specs">ACRYLIC<br>WATERBORNE<br>URETHANE<br>SATIN FINISH</div>
  </div>
</div>
</body>
</html>
```